Biz Card for Harrowfield Property Partners - HFPP

Harrowfield Property Partners is a commercial real estate acquisitions firm. We buy commercial property and need to raise capital from investors for each deal we buy. The vibe needs to be: give us your money, we will multiply it.
Our website: www.hfldpp.com
Competitors are: https://marvenby.com/, https://trellumpartners.com/, http://www.quorvantcapital.com/
Target Market(s)
High Net Worth Individuals, Bankers, Insurance Companies, Commercial Real Estate Brokers.
Industry/Entity Type
Investment Banking
Contact Information for Business Card
Name, Title, Addess, Cell#, Office#, email, website
Requirements
Must have
- use one of our logos. See website for look and feel: www.hfldpp.com
Nice to have
- see website: www.hfldpp.com

```html
<!DOCTYPE html>
<html lang="en">
<head>
<meta charset="utf-8">
<title>Harrowfield Property Partners – Business Card</title>
<link href="https://fonts.googleapis.com/css2?family=Open+Sans:wght@300;400;700&display=swap" rel="stylesheet">
<style>
  :root {
    --navy: #0d2840;
    --white: #ffffff;
    --ink: #0d2840;
    --muted: #4a4f55;
    --stage: #e6e6e4;
  }
  html, body { margin: 0; padding: 0; overflow: hidden; }
  body {
    width: 1200px; height: 900px;
    background: var(--stage);
    font-family: "Open Sans", sans-serif;
    position: relative;
  }
  .card {
    position: absolute;
    left: 320px;
    width: 560px; height: 320px;
    box-shadow: 0 6px 18px rgba(0,0,0,.18);
    overflow: hidden;
  }
  .card--back { top: 90px; background: var(--navy); }
  .card--front { top: 490px; background: var(--white); }

  .brand { position: absolute; display: flex; align-items: center; gap: 14px; }
  .brand__dot { border-radius: 50%; flex: none; }
  .brand__text { font-weight: 300; letter-spacing: .22em; text-transform: uppercase; line-height: 1.2; }
  .brand__name { display: block; }
  .brand__sub { display: block; font-size: .42em; letter-spacing: .34em; margin-top: 4px; }

  .card--back .brand { left: 0; right: 0; top: 0; bottom: 0; justify-content: center; }
  .card--back .brand__dot { width: 84px; height: 84px; background: var(--white); }
  .card--back .brand__text { color: var(--white); font-size: 30px; }

  .card--front .brand { right: 36px; top: 36px; }
  .card--front .brand__dot { width: 56px; height: 56px; background: var(--navy); }
  .card--front .brand__text { color: var(--navy); font-size: 20px; }

  .rule { position: absolute; height: 1px; background: var(--navy); }
  .rule--main { left: 230px; right: 40px; top: 150px; }
  .rule--name { left: 36px; width: 190px; top: 226px; }

  .person { position: absolute; left: 36px; top: 170px; }
  .person__name { margin: 0; font-weight: 700; font-size: 20px; color: var(--ink); letter-spacing: .01em; text-transform: uppercase; }
  .person__title { margin: 0; font-size: 14px; color: var(--muted); }

  .contacts { position: absolute; left: 36px; top: 236px; margin: 0; padding: 0; list-style: none; }
  .contacts li { display: flex; align-items: center; gap: 8px; font-size: 13px; color: var(--muted); line-height: 21px; }
  .contacts svg { width: 12px; height: 12px; fill: var(--navy); flex: none; }

  .address { position: absolute; right: 40px; top: 162px; margin: 0; text-align: right; font-size: 13px; color: var(--muted); line-height: 19px; font-style: normal; }

  .web-tab {
    position: absolute; right: 0; bottom: 0;
    width: 190px; height: 40px;
    background: var(--navy); color: var(--white);
    font-size: 13px; display: flex; align-items: center; justify-content: center;
  }
</style>
</head>
<body>
  <section class="card card--back" aria-label="Card back">
    <div class="brand">
      <span class="brand__dot"></span>
      <span class="brand__text">
        <span class="brand__name">Harrowfield</span>
        <span class="brand__sub">Property Partners</span>
      </span>
    </div>
  </section>

  <section class="card card--front" aria-label="Card front">
    <div class="brand">
      <span class="brand__dot"></span>
      <span class="brand__text">
        <span class="brand__name">Harrowfield</span>
        <span class="brand__sub">Property Partners</span>
      </span>
    </div>

    <div class="rule rule--main"></div>

    <div class="person">
      <p class="person__name">Daniel Ortvale</p>
      <p class="person__title">President</p>
    </div>
    <div class="rule rule--name"></div>

    <ul class="contacts">
      <li>
        <svg viewBox="0 0 12 12"><path d="M3 0h6a1 1 0 0 1 1 1v10a1 1 0 0 1-1 1H3a1 1 0 0 1-1-1V1a1 1 0 0 1 1-1zm0 1.5v8h6v-8z"/></svg>
        (555) 214-7390
      </li>
      <li>
        <svg viewBox="0 0 12 12"><path d="M2.4 0.6l2 2-1 1.6a7 7 0 0 0 4.4 4.4l1.6-1 2 2-1.4 1.8C5 11 1 7 0.6 2z"/></svg>
        (555) 214-7391
      </li>
      <li>
        <svg viewBox="0 0 12 12"><path d="M0 2h12v8H0zm1 1v.4l5 3.2 5-3.2V3z"/></svg>
        info@hfldpp.com
      </li>
    </ul>

    <address class="address">418 Brennick Ave, Suite 900<br>Larchmont Bay, FL 33990</address>

    <div class="web-tab">www.hfldpp.com</div>
  </section>
</body>
</html>
```